HARLOWE CONSERVATORY SAXOPHONE SENIOR RECITAL

I need a poster design for my senior saxophone recital. The title of it is "Quill: a Voyage beneath the Edge of Tone". My concept is completely contrasting to the idea of a typical university recital. I'm so put off by the idea of "clap..clap..{play some music}..clap..clap..repeat". My recital is all based off of sound. The music I selected is all very modern (i.e Brem Ostrakel 'Warm from the First Pour' for Saxophone and Coffee Machine). I've included the Chatterbox link so you can see the picture I have in the background. I like the idea of minimal black and white photography. Also, I would like the time / date / location / etc. all included on it. Let your imaginations run wild! It's art for an artist!
https://www.chatterbox-example.net/events/412093857716230/
Target Market(s)
University Students around the Harlowe Conservatory and locals around the art district of South Beach, FL.
Industry/Entity Type
University
Look and feel

```html
<!DOCTYPE html>
<html lang="en">
<head>
<meta charset="utf-8">
<title>Quill: a Voyage beneath the Edge of Tone — Senior Saxophone Recital</title>
<link rel="stylesheet" href="https://fonts.googleapis.com/css2?family=Exo+2:wght@300;400;500;600;700&display=swap">
<style>
  :root {
    --ink: #231f20;
    --paper: #ffffff;
  }
  html, body {
    margin: 0;
    padding: 0;
    overflow: hidden;
    background: var(--ink);
  }
  .poster {
    position: relative;
    width: 849px;
    height: 1200px;
    background: var(--ink);
    overflow: hidden;
    font-family: "Exo 2", sans-serif;
  }
  .instrument-art {
    position: absolute;
    inset: 0;
    width: 849px;
    height: 1200px;
  }
  .instrument-art path { fill: var(--paper); }

  .title, .performer, .recital-kind, .event-details {
    position: absolute;
    margin: 0;
    line-height: 1;
  }
  .title { color: var(--ink); }
  .title span { position: absolute; white-space: nowrap; }
  .title-lead {
    left: 254px; top: 160px;
    font-size: 64px; font-weight: 600; letter-spacing: -0.5px;
  }
  .title-middle {
    left: 231px; top: 224px;
    font-size: 39px; font-weight: 400;
  }
  .title-close {
    left: 398px; top: 262px;
    font-size: 62px; font-weight: 600; letter-spacing: -0.5px;
  }

  .performer {
    left: 312px; top: 390px;
    color: var(--ink);
    font-size: 36px;
    font-weight: 300;
    text-transform: uppercase;
    white-space: nowrap;
  }
  .performer strong { font-weight: 600; }

  .recital-kind {
    left: 0; top: 0;
    color: var(--ink);
    font-size: 23px;
    font-weight: 400;
    text-transform: uppercase;
    letter-spacing: 1px;
  }
  .recital-kind span { position: absolute; white-space: nowrap; }
  .recital-kind .k1 { left: 352px; top: 444px; }
  .recital-kind .k2 { left: 374px; top: 492px; }
  .recital-kind .k3 { left: 398px; top: 540px; }

  .event-details {
    left: 100px; top: 806px;
    color: var(--paper);
    font-size: 27px;
    line-height: 44px;
  }
  .event-details .when { font-weight: 600; display: block; }
  .event-details .where { font-weight: 400; display: block; }
</style>
</head>
<body>
<main class="poster">
  <svg class="instrument-art" viewBox="0 0 849 1200" role="img" aria-label="White silhouette of a saxophone on black">
    <path d="M197,0 H770 V560 Q770,640 600,660 V1060 Q600,1150 480,1150 H400 Q300,1150 300,1060 V660 Q197,640 197,560 Z"/>
  </svg>

  <h1 class="title">
    <span class="title-lead">Quill:</span>
    <span class="title-middle">a Voyage beneath the</span>
    <span class="title-close">Edge of Tone</span>
  </h1>

  <p class="performer">Dorian <strong>Velasquette</strong></p>

  <p class="recital-kind">
    <span class="k1">Senior</span>
    <span class="k2">Saxophone</span>
    <span class="k3">Recital</span>
  </p>

  <p class="event-details">
    <span class="when">Sunday,<br>December 8,<br>2013,<br>2:00 PM</span>
    <span class="where">Marlow T. Penn<br>Recital Hall</span>
  </p>
</main>
</body>
</html>
```